Webdesign für Projektmanagement
Zielgruppe
Projektmanagement und Projektsteuerung von Bauvorhaben für Projektentwickler und Bauträger.
Wesentliche Bereiche sind Wirtschaftliche Steuerung, Steuerung der Baustelle und Bauabläufe sowie Steuerung der Marketing und Vertriebsaktivitäten.
Aufgabenstellung
Orientierung am Logo. Logo und Visitenkarte liegen bei. Schriftart Prelo und Prelo Slab.

```html
<!DOCTYPE html>
<html lang="de">
<head>
<meta charset="utf-8">
<title>Kerwald Real Estate – Projektmanagement</title>
<link href="https://fonts.googleapis.com/css2?family=Raleway:ital,wght@0,300;0,400;0,500;0,600;0,700;1,300;1,400&display=swap" rel="stylesheet">
<style>
  :root {
    --stage: #00243f;
    --navy: #0b2542;
    --gold: #a8914a;
    --gold-bg: #b3a062;
    --gold-dark: #8f7c3f;
    --card: #f2f2f2;
    --text: #4a4a4a;
    --muted: #6e6e6e;
    --line: #ececec;
    --white: #ffffff;
  }
  * { box-sizing: border-box; margin: 0; padding: 0; }
  html, body {
    width: 1036px; height: 1200px; overflow: hidden;
    background: var(--stage);
    font-family: "Raleway", sans-serif;
  }
  .site {
    position: absolute; left: 20px; top: 313px;
    width: 996px; height: 574px;
    display: flex;
    box-shadow: 0 10px 30px rgba(0,0,0,.35);
  }
  /* Sidebar */
  .sidebar {
    width: 152px; height: 100%;
    background: var(--white);
    position: relative;
  }
  .brand {
    position: absolute; left: 23px; top: 54px;
    font-family: "Raleway", sans-serif;
    font-weight: 700; color: var(--navy);
    line-height: 1;
  }
  .brand-name { display: block; font-size: 23px; letter-spacing: -.2px; }
  .brand-sub { display: block; font-size: 10px; margin-top: 3px; letter-spacing: .3px; }
  .nav {
    position: absolute; left: 0; top: 140px; width: 100%;
    list-style: none;
    border-top: 1px solid var(--line);
  }
  .nav li {
    height: 30.5px; border-bottom: 1px solid var(--line);
    display: flex; align-items: center; justify-content: space-between;
    padding: 0 16px 0 23px;
    font-size: 8.7px; letter-spacing: .3px; color: var(--navy);
    text-transform: uppercase;
  }
  .nav li.is-active { color: var(--gold); font-weight: 700; }
  .nav .chevron { width: 5px; height: 8px; }
  .nav li.search { justify-content: flex-start; gap: 7px; color: #9b9b9b; font-style: italic; text-transform: none; font-size: 8.5px; }
  .social {
    position: absolute; left: 33px; bottom: 21px;
    display: flex; gap: 10px;
  }
  .social span { width: 9px; height: 9px; border-radius: 50%; background: var(--navy); display: block; }

  /* Main */
  .main {
    flex: 1; height: 100%; position: relative; overflow: hidden;
  }
  .hero-image {
    position: absolute; inset: 0;
    background: linear-gradient(135deg, #bba96d 0%, #b19c5c 35%, #a8924f 60%, #b7a46a 80%, #9c8848 100%);
  }
  .topbar {
    position: absolute; left: 0; top: 0; right: 0; height: 28px;
    background: rgba(110, 95, 50, .45);
    display: flex; align-items: center; gap: 18px;
    padding-left: 52px;
    font-size: 8.6px; color: var(--white);
  }
  .topbar .item { display: flex; align-items: center; gap: 6px; }
  .topbar svg { width: 10px; height: 10px; }
  .eyebrow {
    position: absolute; left: 52px; top: 184px;
    font-size: 15px; font-weight: 400; color: var(--white); letter-spacing: .2px;
  }
  .headline {
    position: absolute; left: 51px; top: 215px;
    font-size: 49px; font-weight: 300; color: var(--navy);
    line-height: 56px; letter-spacing: .5px;
  }
  .cards {
    position: absolute; left: 53px; top: 374px;
    display: flex; gap: 9px;
  }
  .card {
    width: 199px; height: 141px; background: var(--card);
    position: relative; padding: 10px 12px 0;
  }
  .card-category { font-size: 8.5px; font-style: italic; color: var(--muted); }
  .card-title {
    margin-top: 7px; font-size: 9.6px; font-weight: 500; color: var(--gold);
    line-height: 13px; text-transform: uppercase;
  }
  .card-text { margin-top: 7px; font-size: 8.6px; line-height: 13px; color: var(--text); }
  .card-button {
    position: absolute; right: 0; bottom: 0;
    width: 76px; height: 20px; background: var(--navy);
    color: var(--white); font-size: 7.6px; font-weight: 600; letter-spacing: .3px;
    display: flex; align-items: center; justify-content: center;
  }
  .footer {
    position: absolute; left: 0; right: 0; bottom: 0; height: 35px;
    background: rgba(120, 105, 55, .3);
    display: flex; align-items: center; padding-left: 53px;
    font-size: 8.6px; color: #6f6334;
  }
</style>
</head>
<body>
  <div class="site">
    <aside class="sidebar">
      <div class="brand">
        <span class="brand-name">Kerwald</span>
        <span class="brand-sub">Real Estate</span>
      </div>
      <ul class="nav">
        <li class="is-active">Home</li>
        <li>Leistungen</li>
        <li>Über uns
          <svg class="chevron" viewBox="0 0 5 8"><path d="M1 1l3 3-3 3" fill="none" stroke="#8a8a8a" stroke-width="1"/></svg>
        </li>
        <li>Projekte
          <svg class="chevron" viewBox="0 0 5 8"><path d="M1 1l3 3-3 3" fill="none" stroke="#8a8a8a" stroke-width="1"/></svg>
        </li>
        <li>Partner</li>
        <li>Kontakt</li>
        <li class="search">
          <svg width="7" height="7" viewBox="0 0 8 8"><circle cx="3.2" cy="3.2" r="2.3" fill="none" stroke="#a8914a" stroke-width="1.3"/><path d="M5 5l2.3 2.3" stroke="#a8914a" stroke-width="1.4"/></svg>
          Suchen
        </li>
      </ul>
      <div class="social" aria-label="Soziale Netzwerke">
        <span></span><span></span><span></span><span></span>
      </div>
    </aside>

    <main class="main">
      <div class="hero-image" role="img" aria-label="Gläserne Hochhausfassaden von unten fotografiert, goldfarben getönt"></div>

      <div class="topbar">
        <span class="item">
          <svg viewBox="0 0 10 10"><path d="M2.2 1l1.6 2.1-.9 1c.6 1.2 1.5 2.1 2.7 2.7l1-.9L8.7 7.5 7.8 9C4.5 8.7 1.3 5.5 1 2.2z" fill="#0b2542"/></svg>
          +49 (0)211 - 735 210 48
        </span>
        <span class="item">
          <svg viewBox="0 0 10 10"><circle cx="5" cy="5" r="4" fill="none" stroke="#0b2542" stroke-width="1.2"/><path d="M5 2.6V5h2" fill="none" stroke="#0b2542" stroke-width="1.1"/></svg>
          Mo - Fr 9:00 - 18:00
        </span>
        <span class="item">
          <svg viewBox="0 0 10 10"><rect x="0.5" y="2" width="9" height="6" fill="#0b2542"/><path d="M.8 2.3L5 5.6l4.2-3.3" fill="none" stroke="#b3a062" stroke-width=".8"/></svg>
          info@kerwald.de
        </span>
        <span class="item">
          <svg viewBox="0 0 10 10"><path d="M5 .5a3 3 0 0 1 3 3C8 6 5 9.5 5 9.5S2 6 2 3.5a3 3 0 0 1 3-3z" fill="#0b2542"/><circle cx="5" cy="3.5" r="1" fill="#b3a062"/></svg>
          Lindenhofstr. 14, 40213 Düsseldorf
        </span>
      </div>

      <p class="eyebrow">PROJEKTMANAGEMENT &amp; PROJEKTSTEUERUNG</p>
      <h1 class="headline">WIR REALISIEREN<br>BAUVORHABEN</h1>

      <section class="cards">
        <article class="card">
          <p class="card-category">Betriebswirtschaftliche Planung</p>
          <h2 class="card-title">Stet clita kasd gubergren no sea takimata sanctus est lorem</h2>
          <p class="card-text">Lorem ipsum dolor sit amet, consetetur sadipscing elitr, sed diam nonumy eirmod tempor invidunt ut labore et dolore magna aliquyam erat, sed diam voluptua.</p>
          <span class="card-button">WEITERLESEN</span>
        </article>
        <article class="card">
          <p class="card-category">Steuerung der baulichen Umsetzung</p>
          <h2 class="card-title">Stet clita kasd gubergren no sea takimata sanctus est lorem</h2>
          <p class="card-text">Lorem ipsum dolor sit amet, consetetur sadipscing elitr, sed diam nonumy eirmod tempor invidunt ut labore et dolore magna aliquyam erat, sed diam voluptua.</p>
          <span class="card-button">WEITERLESEN</span>
        </article>
        <article class="card">
          <p class="card-category">Marketing und Vertrieb</p>
          <h2 class="card-title">Stet clita kasd gubergren no sea takimata sanctus est lorem</h2>
          <p class="card-text">Lorem ipsum dolor sit amet, consetetur sadipscing elitr, sed diam nonumy eirmod tempor invidunt ut labore et dolore magna aliquyam erat, sed diam voluptua.</p>
          <span class="card-button">WEITERLESEN</span>
        </article>
      </section>

      <footer class="footer">© 2017 Kerwald Real Estate GmbH - Impressum</footer>
    </main>
  </div>
</body>
</html>
```